Design a custom Workvine Background Banner (JPG, GIF or PNG)

Hello,
I would like a customized background for my Workvine profile. The specifications are as follows:

* File type JPG, GIF or PNG
* No larger than 4MB.
* Pixel dimensions between 1000 X 425 and 4000 X 4000

Workvine provides these further instructions:

If your background image appears blurry or pixelated, please choose an image with a file size as close to the maximum as possible, as images with larger file sizes typically look better. Photos will also look better than images with logos. If your image is still blurry or pixelated, you may want to run it through a compression tool such as Trimage for Windows or ImageOptim for Mac before uploading it to Workvine.

I want a banner that emphasizes that I'm a healthcare CIO and lists the following responsibilities:

HIPAA
Revenue Cycle
EHR
Health IT
ICD-10
Meaningful Use
Integration
Strategy
Security

Let me know if there isn't enough room for all of these and I can pare it down. I'm attaching two examples of how others in my profession have done that. I'm also including my current banner (which I like) and would be great if we somehow incorporate into the design. No worries if we can't.

Target Market(s)

Recruiters and my peers that may be viewing my profile.

Font styles to use
Sans Serif

Requirements
Nice to have
• Would love to incorporate the blue computer vector image that I attached.

```html
<!DOCTYPE html>
<html lang="en">
<head>
<meta charset="utf-8">
<title>Healthcare CIO Profile Banner</title>
<link rel="stylesheet" href="https://fonts.googleapis.com/css2?family=Open+Sans:wght@400&display=swap">
<style>
  :root {
    --bg-light: #9adbe8;
    --bg-mid: #5fbcd6;
    --bg-deep: #3f98bd;
    --band: rgba(255, 255, 255, 0.42);
    --column: rgba(255, 255, 255, 0.28);
    --hipaa: #1f4e5f;
    --revenue: #1f6a30;
    --ehr: #7b3b7d;
    --health-it: #4b5c8e;
    --security: #4a2a7c;
    --strategy: #c97f3a;
    --integration: #b94848;
    --meaningful: #8a7a12;
    --icd: #17a3c9;
  }
  * { margin: 0; padding: 0; box-sizing: border-box; }
  html, body { width: 1200px; height: 510px; overflow: hidden; }
  body { font-family: "Open Sans", Arial, sans-serif; }

  .banner { position: relative; width: 1200px; height: 510px; overflow: hidden; }

  .code-backdrop {
    position: absolute; inset: 0;
    background:
      repeating-linear-gradient(90deg, rgba(255,255,255,0.10) 0 3px, transparent 3px 22px),
      linear-gradient(180deg, var(--bg-light) 0%, var(--bg-mid) 55%, var(--bg-deep) 100%);
  }

  .word { position: absolute; white-space: nowrap; line-height: 1; }

  .band {
    position: absolute; height: 56px; background: var(--band);
    display: flex; align-items: center; justify-content: center;
    font-size: 35px; line-height: 1;
  }
  .band--left { left: 0; width: 278px; }
  .band--right { left: 920px; width: 280px; }

  .echo {
    position: absolute; font-size: 20px; line-height: 1; text-align: center; opacity: 0.75;
  }
  .echo--left { left: 0; width: 278px; }
  .echo--right { left: 920px; width: 280px; }

  .c-hipaa { color: var(--hipaa); }
  .c-revenue { color: var(--revenue); }
  .c-ehr { color: var(--ehr); }
  .c-health { color: var(--health-it); }
  .c-security { color: var(--security); }
  .c-strategy { color: var(--strategy); }
  .c-integration { color: var(--integration); }
  .c-meaningful { color: var(--meaningful); }

  .center-column {
    position: absolute; left: 524px; top: 156px; width: 104px; height: 354px;
    background: var(--column);
  }

  .cloud-health { left: 305px; top: 28px; font-size: 62px; color: var(--health-it); opacity: 0.35; }
  .cloud-hipaa { left: 300px; top: 160px; font-size: 46px; color: var(--hipaa); opacity: 0.85; transform: rotate(-36deg); transform-origin: left top; }
  .cloud-ehr { left: 305px; top: 355px; font-size: 72px; color: var(--ehr); opacity: 0.3; transform: rotate(-32deg); transform-origin: left top; }
  .cloud-revenue { left: 362px; top: 402px; font-size: 17px; color: var(--revenue); opacity: 0.8; }
  .cloud-integration { left: 630px; top: 106px; font-size: 48px; color: var(--integration); opacity: 0.35; }
  .cloud-security { left: 644px; top: 210px; font-size: 74px; color: var(--security); opacity: 0.35; }
  .cloud-icd { left: 548px; top: 488px; font-size: 62px; color: var(--icd); transform: rotate(-90deg); transform-origin: left top; }
  .cloud-meaningful { left: 655px; top: 458px; font-size: 30px; color: var(--meaningful); opacity: 0.85; transform: rotate(-47deg); transform-origin: left top; }
  .cloud-strategy { left: 824px; top: 350px; font-size: 34px; color: var(--strategy); opacity: 0.85; transform: rotate(72deg); transform-origin: left top; }
  .cloud-hipaa-small { left: 660px; top: 468px; font-size: 31px; color: var(--hipaa); opacity: 0.4; }
</style>
</head>
<body>
<main class="banner">
  <div class="code-backdrop" role="img" aria-label="Blue digital backdrop of falling binary code streams"></div>

  <div class="center-column"></div>

  <span class="word cloud-health">Health IT</span>
  <span class="word cloud-hipaa">HIPAA</span>
  <span class="word cloud-ehr">EHR</span>
  <span class="word cloud-revenue">Revenue Cycle</span>
  <span class="word cloud-integration">Integration</span>
  <span class="word cloud-security">Security</span>
  <span class="word cloud-icd">ICD-10</span>
  <span class="word cloud-meaningful">Meaningful Use</span>
  <span class="word cloud-strategy">Strategy</span>
  <span class="word cloud-hipaa-small">HIPAA</span>

  <div class="band band--left c-hipaa" style="top:50px">HIPAA</div>
  <div class="echo echo--left c-hipaa" style="top:126px">HIPAA</div>
  <div class="band band--left c-revenue" style="top:168px">Revenue Cycle</div>
  <div class="echo echo--left c-revenue" style="top:245px">Revenue Cycle</div>
  <div class="band band--left c-ehr" style="top:293px">EHR</div>
  <div class="echo echo--left c-ehr" style="top:363px">EHR</div>
  <div class="band band--left c-health" style="top:400px">Health IT</div>
  <div class="echo echo--left c-health" style="top:474px">Health IT</div>

  <div class="band band--right c-security" style="top:50px">Security</div>
  <div class="echo echo--right c-security" style="top:126px">Security</div>
  <div class="band band--right c-strategy" style="top:170px">Strategy</div>
  <div class="echo echo--right c-strategy" style="top:247px">Strategy</div>
  <div class="band band--right c-integration" style="top:293px">Integration</div>
  <div class="echo echo--right c-integration" style="top:362px">Integration</div>
  <div class="band band--right c-meaningful" style="top:400px">Meaningful Use</div>
  <div class="echo echo--right c-meaningful" style="top:475px">Meaningful Use</div>
</main>
</body>
</html>
```